Business Card Design using new attached logo

We are a family run Plumbing and Heating firm looking to improve our company image with an improved business card and new logo.We are looking to keep the company colour (Blue) involved in our design

Reason: New logo added which needs to be incorporated on designs

Industry/Entity Type

Business

Contact Information for Business Card

See attachment of all info required.

Requirements
Must have
• We have just picked a new company logo which is attached.
• Could you please provide your business card designs using this logo.
• We are looking for the logo on the back as well as the front with all the info required

```html
<!DOCTYPE html>
<html lang="en">
<head>
<meta charset="utf-8">
<title>Hartwell Services Ltd – Business Cards</title>
<link rel="stylesheet" href="https://fonts.googleapis.com/css2?family=Arimo:wght@400;700&display=swap">
<style>
  :root {
    --brand-blue: #2e51a0;
    --brand-orange: #f28634;
    --paper: #ffffff;
    --backdrop: #f2f2f2;
    --shadow: rgba(0, 0, 0, 0.18);
  }
  * { box-sizing: border-box; margin: 0; padding: 0; }
  html, body {
    width: 1200px; height: 1001px; overflow: hidden;
    background: var(--backdrop);
    font-family: "Arimo", Arial, sans-serif;
  }
  .stage { position: relative; width: 1200px; height: 1001px; }

  .card {
    position: absolute;
    width: 640px; height: 420px;
    box-shadow: 10px 12px 0 var(--shadow);
    overflow: hidden;
  }

  /* Front card */
  .card--front { left: 50px; top: 40px; background: var(--brand-blue); }
  .card--front .wordmark {
    position: absolute; left: 0; right: 0; top: 120px;
    text-align: center; color: var(--paper);
  }
  .wordmark__name { font-size: 64px; font-weight: 400; letter-spacing: -1px; line-height: 1; }
  .wordmark__sub { font-size: 26px; font-weight: 400; letter-spacing: 0.5px; margin-top: 6px; }
  .wordmark__dot {
    display: inline-block; width: 22px; height: 22px; border-radius: 50%;
    background: var(--brand-orange); vertical-align: middle; margin-right: 14px;
    position: relative; top: -6px;
  }
  .trades {
    position: absolute; display: flex; align-items: center;
    font-size: 21px; letter-spacing: 1.5px; color: var(--paper);
  }
  .trades__divider { width: 1px; background: var(--paper); margin: 0 12px; align-self: stretch; }
  .card--front .trades { left: 0; right: 0; justify-content: center; top: 300px; height: 110px; align-items: flex-end; padding-bottom: 56px; }
  .card--front .trades__divider { margin-bottom: -56px; }

  /* Back card */
  .card--back { left: 510px; top: 540px; background: var(--paper); display: flex; }
  .back__panel {
    width: 250px; height: 100%; background: var(--brand-orange); position: relative;
  }
  .back__panel .wordmark {
    position: absolute; left: 0; right: 0; top: 150px; text-align: center; color: var(--brand-blue);
  }
  .back__panel .wordmark__name { font-size: 44px; }
  .back__panel .wordmark__sub { font-size: 18px; margin-top: 4px; }
  .back__panel .wordmark__dot { width: 16px; height: 16px; margin-right: 10px; background: var(--paper); top: -4px; }
  .back__panel .trades {
    left: 0; right: 0; justify-content: center; bottom: 0; height: 130px;
    align-items: flex-end; padding-bottom: 34px; font-size: 16px;
  }
  .back__panel .trades__divider { margin-bottom: -34px; }

  .back__details { flex: 1; padding: 44px 34px; color: var(--brand-blue); text-transform: uppercase; }
  .person__name { font-size: 26px; font-weight: 400; letter-spacing: 0.5px; }
  .person__role { font-size: 18px; margin-left: 14px; margin-top: 2px; }
  .address { font-style: normal; font-size: 17px; line-height: 1.3; margin: 44px 0 0 40px; }
  .contact { list-style: none; font-size: 17px; line-height: 1.3; margin: 32px 0 0 40px; }
  .contact__email { text-transform: none; font-size: 15px; }
</style>
</head>
<body>
<main class="stage">
  <section class="card card--front" aria-label="Business card front">
    <div class="wordmark">
      <div class="wordmark__name"><span class="wordmark__dot"></span>HARTWELL</div>
      <div class="wordmark__sub">SERVICES LTD</div>
    </div>
    <div class="trades">
      <span>PLUMBING</span><span class="trades__divider"></span><span>HEATING</span>
    </div>
  </section>

  <section class="card card--back" aria-label="Business card back">
    <div class="back__panel">
      <div class="wordmark">
        <div class="wordmark__name"><span class="wordmark__dot"></span>HARTWELL</div>
        <div class="wordmark__sub">SERVICES LTD</div>
      </div>
      <div class="trades">
        <span>PLUMBING</span><span class="trades__divider"></span><span>HEATING</span>
      </div>
    </div>
    <div class="back__details">
      <h1 class="person__name">Daniel Hartley</h1>
      <p class="person__role">Director</p>
      <address class="address">
        14 Mill Parade,<br>
        Elm Road, Thornbury,<br>
        Surrey TB2 7QL
      </address>
      <ul class="contact">
        <li>Tel: 020 7946 0321</li>
        <li>Fax: 020 7946 0322</li>
        <li>Mobile: 07700 900456</li>
        <li class="contact__email">danielhartley@hartwellservices.co.uk</li>
      </ul>
    </div>
  </section>
</main>
</body>
</html>
```